Webiste Design KLV

Design the website using uploaded content. Design colors should match that of the company logo with an allowance of one more extra color if it makes the website look much better and colorful. Use Technology related stock images in your design.

Target Market(s)

Potential Clients - Companies

Industry/Entity Type

Information Technology

Coding

Coded - Design and coding required

Number of Pages Required

5+ page

Requirements
Must have
• Company Logo Colors
Nice to have
• Professional Look and Feel with Sliders showing professional information technology images

```html
<!DOCTYPE html>
<html lang="en">
<head>
<meta charset="utf-8">
<title>KLV Technologies</title>
<link href="https://fonts.googleapis.com/css2?family=Poppins:wght@400;500;600;700&display=swap" rel="stylesheet">
<style>
:root{
  --orange:#f27420;
  --orange-dark:#d95f0e;
  --ink:#1e1e1e;
  --dark:#222326;
  --darker:#17181a;
  --text:#3a3a3a;
  --white:#ffffff;
  --beige:#e9d6bd;
  --navy:#07142b;
}
*{margin:0;padding:0;box-sizing:border-box}
html,body{width:1200px;height:4640px;overflow:hidden}
body{font-family:'Poppins',sans-serif;color:var(--text);background:var(--white);position:relative}
section,header,footer{position:absolute;left:0;width:1200px}
.btn{position:absolute;background:var(--orange);color:var(--white);font-weight:600;font-size:18px;border-radius:4px;display:flex;align-items:center;justify-content:center;box-shadow:0 4px 10px rgba(0,0,0,.18)}
h2.title{font-weight:700;font-size:31px;color:var(--ink);text-transform:uppercase;letter-spacing:.3px}
.center{text-align:center;left:0;width:1200px}

/* header */
.site-header{top:0;height:85px;background:var(--white)}
.brand{position:absolute;left:99px;top:26px;display:flex;align-items:center;gap:8px;white-space:nowrap}
.brand-dot{width:26px;height:26px;border-radius:50%;background:var(--orange);flex:none}
.brand-name{font-weight:700;font-size:23px;color:var(--orange);line-height:1}
.nav{position:absolute;left:403px;top:30px;display:flex;gap:34px;font-size:15px;color:#333}
.nav .active{color:var(--orange);font-weight:600;border-bottom:2px solid var(--orange);padding-bottom:4px}
.contact-btn{left:956px;top:18px;width:144px;height:49px;font-size:19px}

/* hero */
.hero{top:85px;height:513px;background:radial-gradient(ellipse 700px 120px at 600px 300px,rgba(40,110,220,.45),transparent 70%),linear-gradient(180deg,#030812 0%,#0a1a36 55%,#050b18 100%)}
.hero h1{position:absolute;top:100px;left:0;width:1200px;text-align:center;color:var(--white);font-weight:700;font-size:51px;line-height:60px}
.hero .btn{left:526px;top:227px;width:148px;height:50px;font-size:18px;border-radius:6px}
.dots{position:absolute;top:440px;left:541px;display:flex;gap:14px}
.dots span{width:13px;height:13px;border-radius:50%;background:#8a8f99}
.dots .on{background:var(--orange)}

/* about */
.about{top:598px;height:536px}
.about h2{position:absolute;left:99px;top:60px}
.about p{position:absolute;left:99px;top:104px;width:520px;font-size:13.5px;line-height:31px}
.about .btn{left:99px;top:402px;width:146px;height:46px}
.network-art{position:absolute;left:648px;top:60px;width:432px;height:414px;border-radius:50%;background:radial-gradient(circle at 65% 50%,#2a2a2a 0 28%,#f58a3a 29% 40%,rgba(242,116,32,.18) 41% 70%,transparent 71%)}

/* mission / vision */
.mv{top:1134px;height:432px;background:linear-gradient(135deg,#1d1f24,#2b2e33 60%,#1c1e22)}
.mv-box{position:absolute;top:50px;width:477px;height:326px;border:2px solid var(--orange);text-align:center;color:var(--white)}
.mv-box h3{margin-top:30px;font-size:30px;font-weight:600}
.mv-icon{margin:14px auto 0;width:126px;height:126px;display:block}
.mv-box p{margin:18px auto 0;width:450px;font-size:14.5px;line-height:26px}
.more{color:var(--orange);font-weight:600}

/* values */
.values{top:1566px;height:545px}
.values h2{position:absolute;top:40px}
.values .lead{position:absolute;top:92px;left:150px;width:900px;text-align:center;font-size:14.5px;line-height:31px}
.value{position:absolute;top:171px;width:324px;height:324px;border-radius:50%;background:var(--ink);color:var(--white);text-align:center;display:flex;flex-direction:column;align-items:center;justify-content:center;padding:0 40px}
.value.hot{background:var(--orange);border:4px solid var(--white);z-index:2}
.value h4{font-size:20px;font-weight:600;line-height:31px;margin-top:10px}
.value p{font-size:15px;line-height:31px}
.value p b{font-weight:600}

/* solutions */
.solutions{top:2111px;height:690px;background:linear-gradient(180deg,#dcc3a4 0%,#efe3d2 55%,#f6eee3 100%)}
.solutions h2{position:absolute;top:50px}
.card{position:absolute;top:105px;width:317px;height:520px;background:var(--white);box-shadow:0 4px 14px rgba(0,0,0,.12);text-align:center}
.card-photo{position:absolute;left:6px;top:6px;width:305px;height:205px}
.card-icon{position:absolute;left:119px;top:172px;width:80px;height:80px;border-radius:50%;background:var(--white);display:flex;align-items:center;justify-content:center}
.card-icon span{width:64px;height:64px;border-radius:50%;background:var(--ink);display:block;border-right:4px solid var(--orange)}
.card h4{position:absolute;top:264px;left:0;width:100%;font-size:21px;line-height:26px;font-weight:700;color:var(--ink)}
.card p{position:absolute;top:320px;left:30px;width:257px;font-size:13.5px;line-height:26px}
.card .btn{left:86px;top:441px;width:145px;height:48px}

/* industries */
.industries{top:2801px;height:610px}
.industries h2{position:absolute;left:96px;top:85px}
.industries p{position:absolute;left:96px;top:132px;width:490px;font-size:13.5px;line-height:31px}
.industries .btn{left:99px;top:464px;width:146px;height:47px}
.factory{position:absolute;left:569px;top:68px;width:631px;height:483px;clip-path:polygon(8% 0,100% 0,100% 100%,0 100%);background:linear-gradient(160deg,#5d7489 0%,#a9bccb 40%,#7c8c97 70%,#3b4a55 100%)}

/* partners */
.partners{top:3411px;height:279px;background:var(--darker)}
.partners h2{position:absolute;top:50px;color:var(--white)}
.logos{position:absolute;left:81px;top:112px;display:flex;gap:14px}
.logos div{width:198px;height:106px;background:var(--white);display:flex;align-items:center;justify-content:center}
.logos i{display:block;width:120px;height:34px;border-radius:4px;background:#c9ccd2}
.arrow{position:absolute;color:var(--white);font-size:30px}

/* teams */
.teams{top:3690px;height:558px}
.teams h2{position:absolute;top:55px}
.member{position:absolute;top:108px;width:324px;text-align:center}
.ring{width:324px;height:324px;border-radius:50%;border:2px solid var(--ink);border-left-color:var(--orange);border-bottom-color:var(--orange);display:flex;align-items:center;justify-content:center}
.portrait{width:276px;height:276px;border-radius:50%;border:2px solid var(--ink);background:linear-gradient(180deg,#d9dde2,#8d9399)}
.member h5{margin-top:36px;font-size:21px;font-weight:700;color:var(--ink)}
.teams .arrow{color:var(--ink);top:248px}

/* footer */
.site-footer{top:4248px;height:392px;background:var(--darker);color:var(--white)}
.site-footer .brand{left:99px;top:70px;gap:10px}
.site-footer .brand-name{color:var(--white);font-size:28px}
.site-footer .brand-dot{width:30px;height:30px}
.contact-list{position:absolute;left:99px;top:150px;font-size:14.5px;line-height:43px}
.contact-list div{display:flex;align-items:center;gap:10px}
.fcol{position:absolute;top:72px;font-size:14.5px}
.fcol h6{font-size:19px;font-weight:600;margin-bottom:10px}
.fcol li{list-style:none;line-height:31px}
.subscribe{position:absolute;left:830px;top:122px;width:270px;height:67px;border-radius:34px;background:var(--white);color:#444;font-size:14px;padding-left:30px;display:flex;align-items:center}
.send{position:absolute;right:6px;top:7px;width:54px;height:54px;border-radius:50%;background:var(--orange);display:flex;align-items:center;justify-content:center}
.social{position:absolute;left:837px;top:225px;display:flex;gap:14px}
.social span{width:46px;height:46px;border-radius:50%;border:2px solid var(--white)}
.rule{position:absolute;left:99px;top:333px;width:1001px;height:1px;background:#555}
.copy{position:absolute;top:350px;left:0;width:1200px;text-align:center;font-size:14.5px}
</style>
</head>
<body>

<header class="site-header">
  <div class="brand"><span class="brand-dot"></span><span class="brand-name">KLV Technologies</span></div>
  <nav class="nav"><span class="active">Home</span><span>AboutUs</span><span>Services</span><span>Mission</span><span>Vision</span><span>Our Value</span></nav>
  <div class="btn contact-btn">Contact Us</div>
</header>

<section class="hero" role="img" aria-label="Dark blue digital network of glowing connected points">
  <h1>WELCOME TO<br>KLV TECHNOLOGIES</h1>
  <div class="btn">Get Started</div>
  <div class="dots"><span></span><span></span><span class="on"></span><span></span><span></span></div>
</section>

<section class="about">
  <h2 class="title">About Us</h2>
  <p>KLV Technologies was founded in 2013 as a Private Company. For Most of its initial existence, the company intends to establish close relationships with its various clients, with the intension of expanding throughout South Africa. KLV Technologies is dedicated to leveraging emerging technologies to provide the highest level of quality products and services, customer service, and security. Our Company is built on the assumption that the management of information technology for business is like legal advice or accounting, in that it is not inherently a do-it-yourself prospect, and requires outside expertise to install and implement it.</p>
  <div class="btn">Read More</div>
  <div class="network-art" role="img" aria-label="Orange and black network diagram of connected nodes"></div>
</section>

<section class="mv">
  <div class="mv-box" style="left:99px">
    <h3>MISSION</h3>
    <svg class="mv-icon" viewBox="0 0 126 126"><circle cx="66" cy="63" r="58" fill="var(--orange)"/><circle cx="56" cy="63" r="54" fill="#24262a" stroke="var(--white)" stroke-width="2"/><circle cx="56" cy="63" r="18" fill="none" stroke="var(--white)" stroke-width="3"/><circle cx="56" cy="63" r="6" fill="var(--white)"/></svg>
    <p>To provide and run ICT as well as Engineering solutions and services that allows our customers to focus on achieving their business objectives. <span class="more">READ MORE</span></p>
  </div>
  <div class="mv-box" style="left:623px">
    <h3>VISION</h3>
    <svg class="mv-icon" viewBox="0 0 126 126"><circle cx="66" cy="63" r="58" fill="var(--orange)"/><circle cx="56" cy="63" r="54" fill="#24262a" stroke="var(--white)" stroke-width="2"/><rect x="36" y="44" width="40" height="26" rx="3" fill="none" stroke="var(--white)" stroke-width="3"/><line x1="46" y1="82" x2="66" y2="82" stroke="var(--white)" stroke-width="3"/></svg>
    <p>Our vision is to be the most innovative and preferred ICT and Engineering Company. We therefore intend to grow the internationally.<span class="more">READ MORE</span></p>
  </div>
</section>

<section class="values">
  <h2 class="title center">Our Values</h2>
  <p class="lead">KLV Technologies is committed to the fair and ethical treatment of employees and stakeholders. This is undertaken through implementation of the following company values:</p>
  <div class="value" style="left:133px">
    <svg width="70" height="70" viewBox="0 0 70 70" fill="none" stroke="#fff" stroke-width="3"><rect x="15" y="30" width="40" height="8"/><rect x="10" y="44" width="50" height="8"/><line x1="35" y1="8" x2="35" y2="22"/><line x1="20" y1="14" x2="26" y2="22"/><line x1="50" y1="14" x2="44" y2="22"/></svg>
    <h4>INTEGRITY</h4>
    <p>We believe that all decisions are made with integrity, being honest with self and with others.</p>
  </div>
  <div class="value hot" style="left:438px">
    <svg width="70" height="70" viewBox="0 0 70 70" fill="none" stroke="#fff" stroke-width="3"><circle cx="30" cy="34" r="16"/><path d="M14 34a16 16 0 0 1 32 0"/><rect x="42" y="8" width="22" height="14" rx="3"/></svg>
    <h4>CUSTOMER SERVICE</h4>
    <p>We believe that customers can of and appreciate great, caring service. efforts on this foundation.<b>READ MORE</b></p>
  </div>
  <div class="value" style="left:738px">
    <svg width="70" height="70" viewBox="0 0 70 70" fill="none" stroke="#fff" stroke-width="3"><circle cx="35" cy="30" r="14"/><circle cx="35" cy="30" r="5"/><rect x="14" y="50" width="42" height="10" rx="2"/></svg>
    <h4>CONTINUOUS<br>IMPROVEMENT</h4>
    <p>We believe in not accepting the status quo; we believe in any form.<b>READ MORE</b></p>
  </div>
</section>

<section class="solutions">
  <h2 class="title center">Our Solutions</h2>
  <div class="card" style="left:99px">
    <div class="card-photo" role="img" aria-label="Engineer with a laptop in a blue-lit server room" style="background:linear-gradient(135deg,#0e2036,#2e5478 55%,#122236)"></div>
    <div class="card-icon"><span></span></div>
    <h4>Infrastructure<br>Solutions</h4>
    <p>KLV Technologies has a strong resources, both office-based as well as site-based at customer country.</p>
    <div class="btn">Read More</div>
  </div>
  <div class="card" style="left:441px">
    <div class="card-photo" role="img" aria-label="Support agent wearing a headset at a laptop" style="background:linear-gradient(135deg,#b59a3a,#e2c35e 45%,#6f6a5c)"></div>
    <div class="card-icon"><span></span></div>
    <h4>Converged<br>Communication</h4>
    <p>Converged Communication Systems provides Telephony / Unified Communications solutions sizes.</p>
    <div class="btn">Read More</div>
  </div>
  <div class="card" style="left:783px">
    <div class="card-photo" role="img" aria-label="Hands on a keyboard with glowing cloud icons" style="background:linear-gradient(135deg,#2a2228,#6d3a2a 50%,#1f1b1f)"></div>
    <div class="card-icon"><span></span></div>
    <h4>Managed<br>Print Services</h4>
    <p>KLV Technologies partnership with global leaders Corvane, Kestrel Optic, Tamori, our customers complete peace of mind.</p>
    <div class="btn">Read More</div>
  </div>
</section>

<section class="industries">
  <h2 class="title">Industries</h2>
  <p>Our “Adaptive Urban Traffic Control System (UTC)” is a leading UTC system in the world. It can control urban traffic signal intelligently by traffic data collection, data processing and system optimization. It can mitigate urban traffic congestion by UTC coordinated controlling, and help people to reduce energy consumption, and reduce traffic accidents. The system can connect with series traffic controllers and other NTCIP compatible controllers. It provides software programming interface for developer. The system can be used to build a whole urban management solution with proper transportation planning, traffic operation and control strategy.</p>
  <div class="btn">Read More</div>
  <div class="factory" role="img" aria-label="Wide view of a modern factory floor with machinery"></div>
</section>

<section class="partners">
  <h2 class="title center">Our Partners</h2>
  <span class="arrow" style="left:40px;top:130px">‹</span>
  <div class="logos">
    <div role="img" aria-label="Partner badge"><i></i></div>
    <div role="img" aria-label="Partner badge"><i></i></div>
    <div role="img" aria-label="Partner badge"><i></i></div>
    <div role="img" aria-label="Partner badge"><i></i></div>
    <div role="img" aria-label="Partner badge"><i></i></div>
  </div>
  <span class="arrow" style="left:1138px;top:130px">›</span>
</section>

<section class="teams">
  <h2 class="title center">Our Teams</h2>
  <span class="arrow" style="left:32px">‹</span>
  <div class="member" style="left:88px"><div class="ring"><div class="portrait" role="img" aria-label="Team member portrait"></div></div><h5>Naledi Khoza</h5></div>
  <div class="member" style="left:438px"><div class="ring"><div class="portrait" role="img" aria-label="Team member portrait"></div></div><h5>Thabo Mokoena</h5></div>
  <div class="member" style="left:785px"><div class="ring"><div class="portrait" role="img" aria-label="Team member portrait"></div></div><h5>Lerato Dlamini</h5></div>
  <span class="arrow" style="left:1146px">›</span>
</section>

<footer class="site-footer">
  <div class="brand"><span class="brand-dot"></span><span class="brand-name">KLV Technologies</span></div>
  <div class="contact-list">
    <div><svg width="14" height="16" viewBox="0 0 14 16"><path d="M7 1a5 5 0 0 1 5 5c0 4-5 9-5 9S2 10 2 6a5 5 0 0 1 5-5z" fill="#fff"/></svg>14 Marula Avenue Polokwane 0700.</div>
    <div><svg width="14" height="14" viewBox="0 0 14 14"><path d="M3 1l3 3-2 2c1 2 2 3 4 4l2-2 3 3-2 2C6 13 1 8 1 3z" fill="#fff"/></svg>012 400 7788</div>
    <div><svg width="16" height="12" viewBox="0 0 16 12"><rect width="16" height="12" fill="#fff"/><path d="M0 0l8 6 8-6" stroke="#17181a" fill="none"/></svg>hello@klvtech.co.za</div>
  </div>
  <div class="fcol" style="left:454px"><h6>QUICK LINKS</h6><ul><li>Home</li><li>About Us</li><li>Mission</li><li>Vision</li><li>Services</li><li>Contact</li></ul></div>
  <div class="fcol" style="left:632px"><h6>OTHER LINKS</h6><ul><li>Privacy Policy</li><li>Tearms of use</li><li>Terms &amp; Condition</li><li>FAQs</li></ul></div>
  <div class="fcol" style="left:830px"><h6>SUBSCRIBE TO NEWSLETTER</h6></div>
  <div class="subscribe">Email ID<span class="send"><svg width="24" height="24" viewBox="0 0 24 24"><path d="M2 11L22 2 15 22l-3-8z" fill="#fff"/></svg></span></div>
  <div class="social"><span aria-label="Social link"></span><span aria-label="Social link"></span><span aria-label="Social link"></span><span aria-label="Social link"></span></div>
  <div class="rule"></div>
  <p class="copy">Copyrights@2023.KLV TECHNOLOGIES.All Rights Reserved</p>
</footer>

</body>
</html>
```